Business Card Design

The attached file is what i need on the front of the card. No details to be changed.

On the back could i have as a heading:
We buy for cash $$$
Deceased estates house lots
Antiques, vintage furniture, bikes, kitchenware, automobile, toys,
sports memorabilia, books, records, signage,farm equipment and fashion.

Industry/Entity Type

House

```html
<!DOCTYPE html>
<html lang="en">
<head>
<meta charset="utf-8">
<title>2210 Vintage – Business Card</title>
<link rel="stylesheet" href="https://fonts.googleapis.com/css2?family=Rochester&family=Courgette&family=Open+Sans:wght@400;600;700&display=swap">
<style>
  :root {
    --backdrop: #ececec;
    --card-red: #d7373b;
    --card-red-deep: #a8262b;
    --card-grey: #e9e9e9;
    --name-yellow: #e8c245;
    --ink: #2b2b2b;
    --ink-soft: #3a3a3a;
    --accent-red: #d7373b;
    --white: #ffffff;
    --social-blue: #3b5998;
  }
  * { margin: 0; padding: 0; box-sizing: border-box; }
  html, body { width: 1200px; height: 900px; overflow: hidden; }
  body {
    background: var(--backdrop);
    position: relative;
    font-family: "Open Sans", Arial, sans-serif;
  }
  .card {
    position: absolute;
    width: 554px;
    height: 358px;
    box-shadow: 0 4px 10px rgba(0,0,0,0.22);
    overflow: hidden;
  }
  .card--front { left: 322px; top: 50px; background: var(--card-grey); }
  .card--back  { left: 320px; top: 430px; background: var(--card-red); }

  .front-banner {
    position: absolute; left: 0; top: 0; width: 554px; height: 242px;
    background: radial-gradient(ellipse at 50% 45%, var(--card-red) 55%, var(--card-red-deep) 100%);
  }
  .brand-name {
    position: absolute; left: 0; right: 0;
    text-align: center;
    font-family: "Rochester", cursive;
    font-weight: 400;
    color: var(--name-yellow);
    white-space: nowrap;
  }
  .front-banner .brand-name { top: 62px; font-size: 78px; line-height: 1; }
  .tagline {
    position: absolute; left: 0; right: 0; top: 198px;
    text-align: center;
    font-family: "Rochester", cursive;
    font-size: 27px;
    color: var(--white);
    letter-spacing: 0.3px;
  }
  .hours-title {
    position: absolute; left: 43px; top: 243px;
    font-size: 15px; font-weight: 700; color: var(--accent-red);
  }
  .hours {
    position: absolute; left: 66px; top: 266px;
    font-size: 13px; line-height: 17px; color: var(--ink);
  }
  .address {
    position: absolute; left: 35px; top: 300px;
    font-size: 13px; line-height: 17px; color: var(--ink);
  }
  .web {
    position: absolute; right: 40px; top: 249px;
    display: flex; align-items: center; gap: 5px;
    font-size: 13.5px; font-weight: 600; color: var(--ink-soft);
  }
  .social-square { width: 26px; height: 26px; background: var(--social-blue); }
  .phones {
    position: absolute; right: 38px; top: 296px;
    text-align: right;
    font-size: 14.5px; font-weight: 700; line-height: 20px; color: var(--ink-soft);
  }

  .back-heading {
    position: absolute; left: 0; right: 0; top: 78px;
    text-align: center;
    font-family: "Courgette", cursive;
    font-size: 15.5px; line-height: 25px;
    color: var(--white);
    font-style: italic;
  }
  .card--back .brand-name { top: 218px; font-size: 60px; line-height: 1; }
</style>
</head>
<body>
  <section class="card card--front">
    <div class="front-banner">
      <div class="brand-name">2210 Vintage</div>
      <div class="tagline">Vintage - Retro&nbsp; Clothing &amp; Collectables</div>
    </div>
    <div class="hours-title">OPEN 6 DAYS A WEEK</div>
    <div class="hours">10:00am - 5:00pm<br>CLOSED TUESDAYS</div>
    <div class="address">2210 Bayside Coast Rd. Harlow 3920<br>Email: info@2210vintage.com.au</div>
    <div class="web">www.2210vintage.com.au <span class="social-square"></span></div>
    <div class="phones">Phone: 59 000 182<br>Mobile: 0400 555 218</div>
  </section>

  <section class="card card--back">
    <div class="back-heading">
      We buy for cash $$$<br>
      Deceased estates house lots<br>
      Antiques, vintage furniture, bikes, kitchenware, automobile, toys,<br>
      sports memorabilia, books, records, signage,farm equipment and fashion.
    </div>
    <div class="brand-name">2210 Vintage</div>
  </section>
</body>
</html>
```